Music Industry Business Needs a Business Card Design

Copper Lantern is an audio mastering company that has been in business for 20 years. Mastering is the final creative step in the music production chain. Our job is to make the music sound as good as it possibly can prior to release to the public. Our world is technical, artistic, precise. We work on everything from independent artists to the music for the Grandfield Cup. We are looking for a new, more modern business card design. I am uploading a copy of our logo, although it doesn't absolutely need to be included in the design.

Target Market(s)

Music Industry Professionals

Industry/Entity Type

Business

Contact Information for Business Card

Address, Phone, Email, Website, Name, Job Title

Font styles to use
Sans Serif

Requirements
Must have
• Sorry, but I don't have any concrete things to request. If I had a clear idea of what I want, I would probably just design something myself. I am looking for fresh input and thought I would try this.
Should not have
• Anything that is typical, such as headphones or the like.

```html
<!DOCTYPE html>
<html lang="en">
<head>
<meta charset="utf-8">
<title>Copper Lantern – Business Card</title>
<link rel="stylesheet" href="https://fonts.googleapis.com/css2?family=Fjalla+One&family=Open+Sans:wght@300;400;600&display=swap">
<style>
  :root {
    --bleed: #7a8f8f;
    --trim: #a3bcbc;
    --card: #0c1112;
    --accent: #3bb6f5;
    --ink: #ffffff;
  }
  html, body {
    margin: 0;
    padding: 0;
    width: 1200px;
    height: 720px;
    overflow: hidden;
    background: var(--bleed);
  }
  .sheet {
    position: relative;
    width: 1200px;
    height: 720px;
    font-family: "Open Sans", Arial, sans-serif;
    color: var(--ink);
  }
  .trim-zone {
    position: absolute;
    left: 40px; top: 40px;
    width: 1120px; height: 640px;
    background: var(--trim);
  }
  .card {
    position: absolute;
    left: 80px; top: 81px;
    width: 1040px; height: 559px;
    background: var(--card);
    border-radius: 48px;
    overflow: hidden;
  }
  .side-band {
    position: absolute;
    left: 61px; top: 0;
    width: 62px; height: 511px;
    background: var(--accent);
    border-radius: 0 0 31px 31px;
  }
  .icon {
    position: absolute;
    left: 80px;
    width: 24px; height: 24px;
    fill: var(--ink);
  }
  .icon--person { left: 70px; top: 86px; width: 44px; height: 44px; }
  .icon--phone { top: 260px; }
  .icon--mail { top: 314px; }
  .icon--web { top: 365px; }
  .icon--home { top: 411px; }
  .person-name {
    position: absolute;
    left: 146px; top: 71px;
    margin: 0;
    font-family: "Fjalla One", "Oswald", sans-serif;
    font-weight: 400;
    font-size: 53px;
    color: var(--accent);
    line-height: 1;
  }
  .person-role {
    position: absolute;
    left: 149px; top: 124px;
    margin: 0;
    font-weight: 400;
    font-size: 26px;
    letter-spacing: 0.3px;
  }
  .contact-list {
    position: absolute;
    left: 147px; top: 0;
    margin: 0; padding: 0;
    list-style: none;
    font-size: 26px;
    font-weight: 400;
    line-height: 36px;
  }
  .contact-list li { position: absolute; left: 0; white-space: nowrap; }
  .contact-phone { top: 254px; }
  .contact-mail { top: 306px; }
  .contact-web { top: 358px; letter-spacing: 1.6px; }
  .contact-address { top: 405px; }
  .brand-name {
    position: absolute;
    right: 68px; top: 320px;
    margin: 0;
    font-weight: 400;
    font-size: 46px;
    letter-spacing: 0.5px;
    text-transform: uppercase;
    line-height: 1;
    white-space: nowrap;
  }
  .brand-bar {
    position: absolute;
    right: 0; top: 359px;
    width: 51px; height: 26px;
    background: var(--accent);
  }
  .zone-label {
    position: absolute;
    margin: 0;
    font-weight: 600;
    font-size: 22px;
    letter-spacing: 0.5px;
    line-height: 1;
  }
  .zone-label--trim { left: 183px; top: 652px; }
  .zone-label--bleed { left: 46px; top: 688px; }
</style>
</head>
<body>
<div class="sheet">
  <div class="trim-zone"></div>

  <div class="card">
    <div class="side-band"></div>

    <svg class="icon icon--person" viewBox="0 0 44 44" aria-hidden="true">
      <path d="M22 4c-6 0-9 4.5-9 10 0 4 1.5 8 4 10v3c-6 1.5-13 4-14 9v4h38v-4c-1-5-8-7.5-14-9v-3c2.5-2 4-6 4-10 0-5.5-3-10-9-10z"/>
    </svg>

    <svg class="icon icon--phone" viewBox="0 0 24 24" aria-hidden="true">
      <path d="M6.5 2.5l3 4.5-2 2c.8 2.8 3 6 5.5 7.5l2-1.8 4.5 3-1.8 3.8C11 20.5 4 12 4.2 4.3z"/>
    </svg>

    <svg class="icon icon--mail" viewBox="0 0 24 24" aria-hidden="true">
      <path d="M2 5h20v14H2zm2 2v.3l8 6 8-6V7zm0 2.8V17h16V9.8l-8 6z"/>
    </svg>

    <svg class="icon icon--web" viewBox="0 0 24 24" aria-hidden="true">
      <path d="M11 1.5a9.5 9.5 0 1 0 1.5 18.9l-.7-2A7.5 7.5 0 0 1 4 12h3.2c.1 1.7.4 3.2.9 4.5h2a15 15 0 0 1-.9-4.5h2.3V10H9.2c.2-2.3.9-4.3 1.8-5.7.9 1.4 1.6 3.4 1.8 5.7h2c-.2-2.2-.8-4.2-1.7-5.7A7.5 7.5 0 0 1 18.4 10h2A9.5 9.5 0 0 0 11 1.5zM7.2 10H4.2a7.5 7.5 0 0 1 5-5.6c-.9 1.5-1.8 3.5-2 5.6zM13 12l9 3.5-3.8 1.3 3 3.5-1.6 1.4-3-3.5-1.6 3.3z"/>
    </svg>

    <svg class="icon icon--home" viewBox="0 0 24 24" aria-hidden="true">
      <path d="M12 2l11 9.5-1.3 1.5L20 11.5V22H4V11.5L2.3 13 1 11.5zM17 4h2v4.5l-2-1.7zM6 10v10h4v-6h4v6h4V10l-6-5.2z"/>
    </svg>

    <h1 class="person-name">Your Name</h1>
    <p class="person-role">GENERAL MANAGER</p>

    <ul class="contact-list">
      <li class="contact-phone">+2&nbsp; (0155) 48-610-37</li>
      <li class="contact-mail">hello@copperlantern.com</li>
      <li class="contact-web">www.copperlantern.com</li>
      <li class="contact-address">1847 Halvorsen Street,<br>NW Brookdale, USA</li>
    </ul>

    <p class="brand-name">Copper Lantern</p>
    <div class="brand-bar"></div>
  </div>

  <p class="zone-label zone-label--trim">TRIM AREA</p>
  <p class="zone-label zone-label--bleed">BLEED AREA</p>
</div>
</body>
</html>
```